Home Page Graphic/Animation (Marketing)

Brightpath Tutor is a Learning Management System provider. We are in the final stages of building our new website and need help with one key element.

We need to create a graphic with animation that will show up on the front page of our new website. Below are some examples of the style we are aiming for:

https://www.dealvoro.example/
https://www.paperquill.example/
https://www.taskmoro.example/

These are just examples of what we like - We are not asking to create a copy of these - But style elements may be borrowed.

For the graphic/animation, we don’t need actual screenshots of the system shown, but we would like these elements to be artistic/semi-abstract in style, but still be accurate to our software. We would like to limit the use of words in the graphic. Please use the color palette shown in either/both the attached screenshot and/or what you see in the product samples in the video links provided. Here are the sections we’d like to highlight in our system and videos of these sections, which will help you understand what our system looks like:

* Administrator LMS – Adding a course (please include a little pop-up with a certificate of completion or a badge) - https://www.brightpathtutor.example/resources/video-detail/how-to-create-an-online-course1
* Administrator LMS – Assigning or editing a Learner page - https://www.brightpathtutor.example/resources/video-detail/updated-directed-learning-feature
* Administrator LMS – Running a report - https://www.vidstreamly.example/watch?v=qRtKm82bXyP&t=1s
* Learner LMS – Clicking through the Learning Paths page to find and take a course (please include our circle progress bars) - https://www.brightpathtutor.example/resources/video-detail/brightpath-tutor-lms-user-overview

I have attached a screenshot of our new home page with the area where this graphic/animation will be placed.

Ultimately, this graphic/animation will mainly serve as eye candy. We want it to be something that makes our product feel well-designed, and technical and draws folks to want to learn more - All without being overly distracting. Think about how this animation can tell a subconscious story.

Target Market(s)

Corporate Education

Industry/Entity Type

E-Learning / Learning Management System

Number of Pages Required

1 page

Font styles to use
Sans Serif

Requirements
Must have
• Animation / Motion Graphic

```html
<!DOCTYPE html>
<html lang="en">
<head>
<meta charset="utf-8">
<title>Brightpath Tutor – Home Hero Graphic</title>
<link rel="stylesheet" href="https://fonts.googleapis.com/css2?family=Poppins:wght@400;500;600;700&display=swap">
<style>
  :root{
    --bg:#eef9fb;
    --halo:#dcefd8;
    --frame:#f3f6f7;
    --frame-line:#e2e8ea;
    --card:#ffffff;
    --card-line:#e6eaec;
    --ink:#2f4a4f;
    --ink-soft:#5b6e72;
    --dark:#2f4a4f;
    --green:#8cc63f;
    --cyan:#2bbfd8;
    --skeleton:#eef0f1;
    --icon:#3d5256;
    --medal-a:#f6c445;
    --medal-b:#ee8a4a;
  }
  *{box-sizing:border-box;margin:0;padding:0}
  html,body{width:1200px;height:676px;overflow:hidden;background:var(--bg);font-family:"Poppins",sans-serif;color:var(--ink)}
  .canvas{position:relative;width:1200px;height:676px;overflow:hidden;background:var(--bg)}
  .abs{position:absolute}
  .pin-backdrop{left:0;top:0;width:1200px;height:676px}
  .app-frame{left:291px;top:130px;width:595px;height:381px;background:var(--frame);border:1px solid var(--frame-line);border-radius:8px}
  .sidebar{left:291px;top:130px;width:41px;height:381px;border-right:1px solid var(--frame-line)}
  .nav-home{left:301px;top:182px;width:23px;height:23px;border-radius:4px;background:var(--green);display:flex;align-items:center;justify-content:center}
  .nav-icon{left:302px;width:21px;height:21px}
  .lang-pop{left:645px;top:81px;width:201px;height:54px;background:var(--card);border:1px solid var(--card-line);border-radius:6px}
  .lang-title{left:668px;top:92px;font-size:11.5px;font-weight:600}
  .lang-pill{left:666px;top:112px;width:146px;height:33px;border-radius:17px;background:var(--dark);color:#fff;font-size:11px;display:flex;align-items:center;padding-left:14px;gap:6px}
  .lang-toggle{left:774px;top:109px;width:40px;height:40px;border-radius:50%;background:var(--green);display:flex;align-items:center;justify-content:center}
  .topbar{left:354px;top:157px;width:571px;height:47px;background:var(--card);border:1px solid var(--card-line);border-radius:24px}
  .brand-dot{left:365px;top:169px;width:24px;height:24px;border-radius:50%;background:var(--cyan)}
  .brand-name{left:396px;top:170px;font-size:15px;font-weight:600;color:var(--ink)}
  .search-hint{left:716px;top:174px;font-size:10px;color:var(--ink-soft);display:flex;align-items:center;gap:4px}
  .divider{left:800px;top:174px;width:1px;height:16px;background:var(--card-line)}
  .user-role{left:821px;top:169px;font-size:9px;color:var(--ink-soft);line-height:1.1}
  .user-name{left:821px;top:179px;font-size:11px;font-weight:700}
  .avatar{border-radius:50%}
  .avatar-top{left:888px;top:169px;width:25px;height:25px;background:linear-gradient(135deg,#5a4a40,#2f2a28)}
  .courses{left:356px;top:219px;width:516px;height:92px;background:var(--card);border:1px solid var(--card-line);border-radius:6px}
  .courses-title{left:373px;top:232px;font-size:11px;font-weight:600}
  .name-search{left:371px;top:259px;width:247px;height:38px;border:1px solid #dde2e4;border-radius:3px;font-size:9.5px;color:var(--ink-soft);padding:12px 17px}
  .btn{top:259px;height:38px;border-radius:3px;color:#fff;font-size:9.5px;font-weight:600;display:flex;align-items:center;justify-content:center;gap:5px;letter-spacing:.1px}
  .btn-add{left:626px;width:102px;background:var(--cyan)}
  .btn-tools{left:735px;width:123px;background:var(--green)}
  .card{background:var(--card);border:1px solid var(--card-line);border-radius:6px}
  .badge-card{left:356px;top:324px;width:175px;height:175px}
  .badge-backdrop{left:362px;top:330px;width:161px;height:81px;background:var(--skeleton);border-radius:4px}
  .badge-art{left:400px;top:337px;width:100px;height:129px;border-radius:4px;background:linear-gradient(180deg,var(--medal-a),var(--medal-b))}
  .bar{background:var(--skeleton);border-radius:5px}
  .list-card{left:540px;top:324px;width:373px;height:175px}
  .row-line{left:556px;width:330px;height:1px;background:#f0f2f3}
  .pill-track{left:864px;width:34px;height:7px;border-radius:4px;background:#f0f3ef}
  .pill-fill{left:872px;width:17px;height:6px;border-radius:3px;background:var(--green)}
  .student-card{background:var(--card);border:1px solid var(--card-line);border-radius:6px;box-shadow:0 6px 20px rgba(47,74,79,.08)}
  .student-head{background:var(--dark);border-radius:4px 4px 0 0}
  .s-role{font-size:10px;color:#c9d6d8}
  .s-name{font-size:12px;font-weight:700;color:#fff}
  .online{width:9px;height:9px;border-radius:50%;background:var(--green);border:1.5px solid #fff}
</style>
</head>
<body>
<div class="canvas">
  <svg class="abs pin-backdrop" viewBox="0 0 1200 676">
    <path d="M545 490 A253 253 0 1 1 879 490 L712 637 Z" fill="var(--halo)"/>
  </svg>

  <div class="abs app-frame"></div>
  <div class="abs sidebar"></div>
  <div class="abs nav-home">
    <svg width="13" height="13" viewBox="0 0 24 24"><path d="M12 3 2 12h3v9h5v-6h4v6h5v-9h3z" fill="#fff"/></svg>
  </div>
  <svg class="abs nav-icon" style="top:218px" viewBox="0 0 24 24" fill="none" stroke="var(--icon)" stroke-width="1.4"><rect x="6" y="3" width="12" height="18" rx="1"/><path d="M9 3v18M12 3v6l1.5-1 1.5 1V3"/></svg>
  <svg class="abs nav-icon" style="top:249px" viewBox="0 0 24 24" fill="none" stroke="var(--icon)" stroke-width="1.4"><circle cx="12" cy="8" r="4"/><path d="M5 21v-2a5 5 0 0 1 5-5h4a5 5 0 0 1 5 5v2z"/></svg>
  <svg class="abs nav-icon" style="top:279px" viewBox="0 0 24 24" fill="none" stroke="var(--icon)" stroke-width="1.4"><path d="M3 3v18h18M6 20V8h3v12M11 20V5h3v15M16 20v-8h3v8"/></svg>
  <svg class="abs nav-icon" style="top:309px" viewBox="0 0 24 24" fill="none" stroke="var(--icon)" stroke-width="1.4"><rect x="3" y="6" width="18" height="13" rx="1"/><path d="m3 7 9 7 9-7"/><circle cx="21" cy="4" r="2" fill="var(--green)" stroke="none"/></svg>
  <svg class="abs nav-icon" style="top:338px" viewBox="0 0 24 24" fill="none" stroke="var(--icon)" stroke-width="1.4"><path d="M3 10h18l-2 10H5zM7 10l3-6M17 10l-3-6M9 13v5M12 13v5M15 13v5"/></svg>

  <div class="abs lang-pop"></div>
  <div class="abs lang-title">Worlwide Language</div>
  <div class="abs lang-pill">
    <svg width="14" height="14" viewBox="0 0 24 24" fill="none" stroke="#fff" stroke-width="1.5"><circle cx="12" cy="12" r="9"/><path d="M3 12h18M12 3c3 3 3 15 0 18M12 3c-3 3-3 15 0 18"/></svg>
    English
  </div>
  <div class="abs lang-toggle">
    <svg width="12" height="12" viewBox="0 0 24 24" fill="none" stroke="#fff" stroke-width="2.5"><path d="m5 9 7 7 7-7"/></svg>
  </div>

  <div class="abs topbar"></div>
  <div class="abs brand-dot"></div>
  <div class="abs brand-name">Brightpath Tutor</div>
  <div class="abs search-hint">
    <svg width="12" height="12" viewBox="0 0 24 24" fill="none" stroke="var(--ink)" stroke-width="2.5"><circle cx="10" cy="10" r="7"/><path d="m15 15 6 6"/></svg>
    Search Here
  </div>
  <div class="abs divider"></div>
  <div class="abs user-role">Student</div>
  <div class="abs user-name">Corin M.</div>
  <div class="abs avatar avatar-top" role="img" aria-label="Student profile photo"></div>

  <div class="abs courses"></div>
  <div class="abs courses-title">Courses</div>
  <div class="abs name-search">Search by Name</div>
  <div class="abs btn btn-add">ADD COURSE
    <svg width="10" height="10" viewBox="0 0 10 10" stroke="#fff" stroke-width="1.8"><path d="M5 0v10M0 5h10"/></svg>
  </div>
  <div class="abs btn btn-tools">CONTENT TOOLS</div>

  <div class="abs card badge-card"></div>
  <div class="abs badge-backdrop"></div>
  <div class="abs badge-art" role="img" aria-label="Illustration of a gold completion medal with ribbon"></div>
  <div class="abs bar" style="left:420px;top:478px;width:103px;height:12px"></div>

  <div class="abs card list-card"></div>
  <div class="abs bar" style="left:556px;top:339px;width:297px;height:8px"></div>
  <div class="abs pill-track" style="top:339px"></div><div class="abs pill-fill" style="top:340px"></div>
  <div class="abs row-line" style="top:360px"></div>
  <div class="abs bar" style="left:556px;top:374px;width:297px;height:8px"></div>
  <div class="abs pill-track" style="top:374px"></div><div class="abs pill-fill" style="top:375px"></div>
  <div class="abs row-line" style="top:395px"></div>
  <div class="abs bar" style="left:556px;top:409px;width:297px;height:8px"></div>
  <div class="abs pill-track" style="top:409px"></div><div class="abs pill-fill" style="top:410px"></div>
  <div class="abs row-line" style="top:430px"></div>
  <div class="abs bar" style="left:556px;top:444px;width:297px;height:8px"></div>
  <div class="abs pill-track" style="top:444px"></div><div class="abs pill-fill" style="top:445px"></div>
  <div class="abs row-line" style="top:465px"></div>
  <div class="abs bar" style="left:556px;top:479px;width:297px;height:8px"></div>
  <div class="abs pill-track" style="top:479px"></div><div class="abs pill-fill" style="top:479px"></div>

  <div class="abs student-card" style="left:251px;top:364px;width:170px;height:253px"></div>
  <div class="abs student-head" style="left:258px;top:371px;width:156px;height:61px"></div>
  <div class="abs avatar" role="img" aria-label="Student profile photo" style="left:272px;top:383px;width:38px;height:38px;background:linear-gradient(135deg,#c9dce8,#3f6fa5)"></div>
  <div class="abs online" style="left:299px;top:411px"></div>
  <div class="abs s-role" style="left:317px;top:389px">Student</div>
  <div class="abs s-name" style="left:317px;top:401px">Corin M.</div>
  <div class="abs bar" style="left:269px;top:448px;width:133px;height:8px"></div>
  <div class="abs bar" style="left:269px;top:465px;width:133px;height:8px"></div>
  <div class="abs bar" style="left:269px;top:483px;width:133px;height:8px"></div>
  <div class="abs" style="left:270px;top:519px;width:45px;height:8px;border-radius:4px;background:var(--green)"></div>
  <div class="abs" style="left:319px;top:519px;width:83px;height:8px;border-radius:4px;background:var(--cyan)"></div>
  <div class="abs bar" style="left:269px;top:540px;width:133px;height:8px"></div>
  <div class="abs bar" style="left:269px;top:557px;width:133px;height:8px"></div>
  <div class="abs" style="left:321px;top:576px;width:30px;height:30px;border-radius:50%;background:var(--skeleton)"></div>

  <div class="abs student-card" style="left:684px;top:376px;width:169px;height:177px"></div>
  <div class="abs student-head" style="left:684px;top:376px;width:169px;height:61px"></div>
  <div class="abs avatar" role="img" aria-label="Student profile photo" style="left:697px;top:388px;width:38px;height:38px;background:linear-gradient(135deg,#f4e3e6,#d9a9b4)"></div>
  <div class="abs online" style="left:725px;top:417px"></div>
  <div class="abs s-role" style="left:743px;top:393px">Student</div>
  <div class="abs s-name" style="left:743px;top:406px">Corin M.</div>
  <div class="abs bar" style="left:701px;top:460px;width:133px;height:8px"></div>
  <div class="abs bar" style="left:701px;top:482px;width:133px;height:8px"></div>
  <div class="abs bar" style="left:701px;top:503px;width:133px;height:8px"></div>
  <div class="abs bar" style="left:701px;top:524px;width:133px;height:8px"></div>
</div>
</body>
</html>
```